This is a laser engraving business. I’m looking for a business card that includes a minimalist laser logo/design with the company name Brisk Harbor Crafts and telephone number 654-210-3378 and email briskharborcrafts@mailrove.com

Industry/Entity Type

Laser engraving

Contact Information for Business Card

Laser logo/design that represents laser engraving

```html
<!DOCTYPE html>
<html lang="en">
<head>
<meta charset="utf-8">
<title>Brisk Harbor Crafts – Business Card</title>
<link href="https://fonts.googleapis.com/css2?family=Montserrat:wght@400;500;800&display=swap" rel="stylesheet">
<style>
  :root {
    --stage: #1c1c1e;
    --card: #050505;
    --red: #d7212b;
    --white: #ffffff;
    --grey: #d9d9d9;
  }
  * { margin: 0; padding: 0; box-sizing: border-box; }
  html, body { width: 1200px; height: 866px; overflow: hidden; }
  body {
    background: var(--stage);
    font-family: "Montserrat", Arial, sans-serif;
    position: relative;
  }
  .card {
    position: absolute;
    left: 270px;
    width: 660px;
    height: 377px;
    background: var(--card);
    border-radius: 4px;
    overflow: hidden;
  }
  .card-front { top: 40px; }
  .card-back { top: 449px; }

  .brand {
    position: absolute;
    display: flex;
    align-items: center;
    gap: 14px;
  }
  .brand-dot {
    border-radius: 50%;
    background: var(--red);
    flex: none;
  }
  .brand-name {
    color: var(--white);
    font-weight: 800;
    text-transform: uppercase;
    letter-spacing: 2px;
    line-height: 1.05;
  }
  .card-front .brand { left: 50%; top: 50%; transform: translate(-50%, -50%); }
  .card-front .brand-dot { width: 46px; height: 46px; }
  .card-front .brand-name { font-size: 34px; }

  .card-back .brand { right: 60px; top: 70px; gap: 10px; }
  .card-back .brand-dot { width: 28px; height: 28px; }
  .card-back .brand-name { font-size: 21px; }

  .divider-top {
    position: absolute;
    left: 250px;
    right: 0;
    top: 170px;
    height: 2px;
    background: var(--red);
  }
  .contact-block { position: absolute; left: 56px; top: 210px; }
  .person-name {
    color: var(--red);
    font-weight: 800;
    font-size: 27px;
    letter-spacing: 0.5px;
    text-transform: uppercase;
  }
  .person-role {
    color: var(--grey);
    font-size: 16px;
    font-weight: 400;
    margin-top: 2px;
  }
  .divider-name {
    width: 200px;
    height: 1.5px;
    background: var(--red);
    margin: 14px 0 14px;
  }
  .contact-line {
    display: flex;
    align-items: center;
    gap: 14px;
    color: var(--white);
    font-size: 15px;
    font-weight: 400;
    margin-bottom: 8px;
  }
  .contact-line svg { width: 16px; height: 16px; fill: var(--red); flex: none; }
</style>
</head>
<body>
  <section class="card card-front">
    <div class="brand">
      <span class="brand-dot"></span>
      <span class="brand-name">Brisk Harbor<br>Crafts</span>
    </div>
  </section>

  <section class="card card-back">
    <div class="brand">
      <span class="brand-dot"></span>
      <span class="brand-name">Brisk Harbor<br>Crafts</span>
    </div>
    <div class="divider-top"></div>

    <div class="contact-block">
      <h1 class="person-name">Marcus Hale</h1>
      <p class="person-role">Managing Director</p>
      <div class="divider-name"></div>
      <p class="contact-line">
        <svg viewBox="0 0 24 24" aria-hidden="true"><path d="M6.6 10.8a15.1 15.1 0 0 0 6.6 6.6l2.2-2.2a1 1 0 0 1 1-.25 11.4 11.4 0 0 0 3.6.57 1 1 0 0 1 1 1V20a1 1 0 0 1-1 1A17 17 0 0 1 3 4a1 1 0 0 1 1-1h3.5a1 1 0 0 1 1 1c0 1.25.2 2.45.57 3.57a1 1 0 0 1-.25 1z"/></svg>
        654-210-3378
      </p>
      <p class="contact-line">
        <svg viewBox="0 0 24 24" aria-hidden="true"><path d="M2 5h20v14H2z M2 5l10 8 10-8" /><path d="M2 5h20L12 12.5z" fill="#050505" opacity="0.35"/></svg>
        briskharborcrafts@mailrove.com
      </p>
    </div>
  </section>
</body>
</html>
```